Copperleaf Motorized Shade Business Card

Hello, we've had our logo made. Now we are looking for a clean and cool looking business card. One side can just be the logo with any design elements that might look good with it. The other side will be Name, Phone Number and Email. There will not be an address on the card.

```html
<!DOCTYPE html>
<html lang="en">
<head>
<meta charset="utf-8">
<title>Copperleaf Motorized Shade – Business Card</title>
<link href="https://fonts.googleapis.com/css2?family=Bebas+Neue&family=Libre+Franklin:wght@400&display=swap" rel="stylesheet">
<style>
  :root {
    --navy: #003c73;
    --sun: #fdc313;
    --sky: #00a9e8;
    --white: #ffffff;
    --ink: #2a2a2a;
    --backdrop: #dde8f1;
  }
  html, body {
    margin: 0;
    padding: 0;
    width: 1200px;
    height: 1200px;
    overflow: hidden;
    background: var(--backdrop);
  }
  .canvas {
    position: relative;
    width: 1200px;
    height: 1200px;
  }
  .card {
    position: absolute;
    left: 283px;
    width: 634px;
    height: 362px;
    overflow: hidden;
  }
  .card--front { top: 174px; background: var(--white); }
  .card--back  { top: 610px; background: var(--navy); }

  .wordmark {
    position: absolute;
    font-family: 'Bebas Neue', sans-serif;
    font-weight: 400;
    line-height: 0.95;
    text-align: center;
    margin: 0;
  }
  .card--front .wordmark {
    left: 60px;
    top: 112px;
    width: 230px;
    color: var(--navy);
    font-size: 50px;
  }
  .card--front .wordmark small {
    display: block;
    font-size: 20px;
    letter-spacing: 4px;
    margin-top: 4px;
  }
  .card--back .wordmark {
    left: 0;
    top: 118px;
    width: 634px;
    color: var(--white);
    font-size: 108px;
  }
  .card--back .wordmark small {
    display: block;
    font-size: 34px;
    letter-spacing: 9px;
    margin-top: 6px;
  }

  .divider {
    position: absolute;
    left: 316px;
    top: 94px;
    width: 1px;
    height: 123px;
    background: var(--navy);
  }
  .divider::before {
    content: "";
    position: absolute;
    left: 0;
    top: 0;
    width: 3px;
    height: 22px;
    background: var(--navy);
  }

  .contact {
    position: absolute;
    left: 343px;
    top: 90px;
    font-family: 'Libre Franklin', sans-serif;
    color: var(--ink);
  }
  .contact__name {
    margin: 0;
    font-family: 'Bebas Neue', sans-serif;
    font-weight: 400;
    font-size: 33px;
    line-height: 1;
    color: var(--navy);
  }
  .contact__role {
    margin: 2px 0 0;
    font-size: 15.5px;
  }
  .contact__list {
    list-style: none;
    margin: 26px 0 0;
    padding: 0;
    font-size: 15.5px;
  }
  .contact__list li {
    display: flex;
    align-items: center;
    gap: 9px;
    height: 21px;
  }
  .contact__list svg { width: 11px; height: 11px; fill: var(--navy); }

  .swoosh {
    position: absolute;
    left: 0;
    top: 0;
    width: 634px;
    height: 362px;
  }
</style>
</head>
<body>
<main class="canvas">
  <section class="card card--front" aria-label="Business card front">
    <p class="wordmark">Copperleaf<small>Motorized Shade</small></p>
    <span class="divider"></span>
    <div class="contact">
      <h1 class="contact__name">Daniel Reed Carter</h1>
      <p class="contact__role">Manager / Owner</p>
      <ul class="contact__list">
        <li>
          <svg viewBox="0 0 12 12" aria-hidden="true"><path d="M2.5 0.5 L4.6 0.5 L5.2 3.4 L3.8 4.5 Q5 7.2 7.5 8.3 L8.6 7 L11.5 7.6 L11.5 9.6 Q11.5 11.5 9.4 11.5 Q0.5 10.5 0.5 2.6 Q0.5 0.5 2.5 0.5Z"/></svg>
          <span>+1 555 014 2290</span>
        </li>
        <li>
          <svg viewBox="0 0 12 12" aria-hidden="true"><path d="M0.5 3 L6 7 L11.5 3 L11.5 11 L0.5 11Z M1 1.5 L11 1.5 L6 5.3Z"/></svg>
          <span>dcarter@copperleafshade.com</span>
        </li>
      </ul>
    </div>
    <svg class="swoosh" viewBox="0 0 634 362" aria-hidden="true">
      <path d="M66 318 Q317 238 568 318 Q317 262 66 318Z" fill="var(--sun)"/>
      <path d="M0 346 Q317 250 634 346 L634 362 L0 362Z" fill="var(--navy)"/>
    </svg>
  </section>

  <section class="card card--back" aria-label="Business card back">
    <p class="wordmark">Copperleaf<small>Motorized Shade</small></p>
  </section>
</main>
</body>
</html>
```